Tindalee Pure Honey

Dear Friends I would like a label to designed for a new brand we wish to create called TINDALEE pure honey.

I need 2 versions

Version 1 - normal general version for every buyer

Version 2 - this is a KIDS HONEY version and must be designed
specifically to attract Kids and be fun.

Version 1 size is 127mm wide x 60mm high

Version 2 size is 168mm long x 60mm wide

labels must be set up with following info on the face of the product

TINDALEE

100% Pure Honey

AUSTRALIAN

For version 2 we must have the words KIDS HONEY on the face.

Best regards

Selim

Product

• Please note the label layout is landscape so 127mm wide x 60mm high

```html
<!DOCTYPE html>
<html lang="en">
<head>
<meta charset="utf-8">
<title>Tindalee Pure Honey – Labels</title>
<link rel="stylesheet" href="https://fonts.googleapis.com/css2?family=Anton&family=Open+Sans:wght@400;700&family=Noto+Serif:wght@700&display=swap">
<style>
  :root {
    --canvas: #ffffff;
    --frame-edge: #f5b52c;
    --frame-mid: #f9dc2c;
    --panel-green: #184d23;
    --glow-green: #6aa51c;
    --honey-light: #fbe43a;
    --honey-deep: #f4b323;
    --text-light: #ffffff;
    --art-tone: #e8c12a;
  }
  html, body {
    margin: 0;
    padding: 0;
    width: 1200px;
    height: 1000px;
    overflow: hidden;
    background: var(--canvas);
  }
  .label-sheet { display: block; width: 1200px; height: 1000px; }
  .brand-name { font-family: "Anton", "Impact", sans-serif; font-size: 40px; letter-spacing: 1px; fill: var(--honey-light); }
  .product-line { font-family: "Open Sans", Arial, sans-serif; font-size: 17px; fill: var(--text-light); }
  .origin { font-family: "Open Sans", Arial, sans-serif; font-weight: 700; font-size: 20px; fill: var(--text-light); }
  .kids-title { font-family: "Noto Serif", Georgia, serif; font-weight: 700; font-size: 25px; fill: var(--text-light); }
  .frame-outer { fill: url(#frameGradient); }
  .brand-mark { fill: var(--honey-light); }
  .honey-drop { fill: url(#dropGradient); }
  .art-area { fill: url(#artGradient); }
</style>
</head>
<body>
<svg class="label-sheet" viewBox="0 0 1200 1000" xmlns="http://www.w3.org/2000/svg">
  <defs>
    <linearGradient id="frameGradient" x1="0" y1="0" x2="0" y2="1">
      <stop offset="0" stop-color="var(--frame-edge)"/>
      <stop offset="0.5" stop-color="var(--frame-mid)"/>
      <stop offset="1" stop-color="var(--frame-edge)"/>
    </linearGradient>
    <radialGradient id="glowStandard" cx="412" cy="600" r="170" gradientUnits="userSpaceOnUse">
      <stop offset="0" stop-color="var(--glow-green)"/>
      <stop offset="1" stop-color="var(--panel-green)"/>
    </radialGradient>
    <radialGradient id="glowKids" cx="788" cy="470" r="220" gradientUnits="userSpaceOnUse">
      <stop offset="0" stop-color="var(--glow-green)"/>
      <stop offset="1" stop-color="var(--panel-green)"/>
    </radialGradient>
    <radialGradient id="dropGradient" cx="0.5" cy="0.65" r="0.6">
      <stop offset="0" stop-color="var(--honey-light)"/>
      <stop offset="1" stop-color="var(--honey-deep)"/>
    </radialGradient>
    <radialGradient id="artGradient" cx="0.5" cy="0.5" r="0.6">
      <stop offset="0" stop-color="var(--honey-light)"/>
      <stop offset="1" stop-color="var(--art-tone)" stop-opacity="0.4"/>
    </radialGradient>
  </defs>

  <!-- Standard label -->
  <g class="label label-standard">
    <rect class="frame-outer" x="258" y="281" width="306" height="647"/>
    <rect class="panel" x="283" y="306" width="256" height="596" fill="url(#glowStandard)"/>
    <circle class="brand-mark" cx="412" cy="410" r="34"/>
    <text class="brand-name" x="412" y="500" text-anchor="middle">TINDALEE</text>
    <path class="honey-drop" d="M412 564 C404 590 379 612 379 632 a33 33 0 0 0 66 0 C445 612 420 590 412 564 Z"/>
    <text class="product-line" x="412" y="712" text-anchor="middle">100% Pure Honey</text>
    <text class="product-line" x="412" y="739" text-anchor="middle">1 litre</text>
    <rect class="art-area" x="383" y="776" width="58" height="52" rx="8" role="img" aria-label="Map outline of Australia"/>
    <text class="origin" x="412" y="864" text-anchor="middle">AUSTRALIAN</text>
  </g>

  <!-- Kids label -->
  <g class="label label-kids">
    <rect class="frame-outer" x="636" y="72" width="305" height="856"/>
    <rect class="panel" x="661" y="97" width="255" height="805" fill="url(#glowKids)"/>
    <circle class="brand-mark" cx="788" cy="190" r="36"/>
    <text class="brand-name" x="788" y="283" text-anchor="middle">TINDALEE</text>
    <rect class="art-area" x="684" y="360" width="178" height="138" rx="20" role="img" aria-label="Cartoon bees around a honeycomb"/>
    <text class="kids-title" x="788" y="533" text-anchor="middle">Kids Honey</text>
    <path class="honey-drop" d="M788 552 C780 578 755 600 755 620 a33 33 0 0 0 66 0 C821 600 796 578 788 552 Z"/>
    <text class="product-line" x="788" y="712" text-anchor="middle">100% Pure Honey</text>
    <text class="product-line" x="788" y="739" text-anchor="middle">1 litre</text>
    <rect class="art-area" x="759" y="776" width="58" height="52" rx="8" role="img" aria-label="Map outline of Australia"/>
    <text class="origin" x="788" y="864" text-anchor="middle">AUSTRALIAN</text>
  </g>
</svg>
</body>
</html>
```